Stonebrook 720 Real Estate Investment Company

We need a business card designed for a real estate investment company named Stonebrook 720. We want to use red#f04a50, orange #f37122 and yellow #fbee3e as the color scheme. The logo colors will need to be modified from the current blue palette. I've attach VitaPathway logo example that captures the color scheme we're going for for Stonebrook 720. Looking for clean Sans Serif fonts.
Contact Information for Business Card
Daniel Furlow
Managing Partner
48317 Whitfield Lane, Suite 510
Tampa, FL 33718
813-555-4870 Mobile
dfurlow@stonebrook720.example
www.stonebrook720.example
Requirements
Must have
- Looking for creative responses.
Nice to have
- Must hit color palette... orange, red, yellow

```html
<!DOCTYPE html>
<html lang="en">
<head>
<meta charset="utf-8">
<title>Stonebrook 720 Business Card</title>
<link href="https://fonts.googleapis.com/css2?family=Roboto:wght@400;500;700&display=swap" rel="stylesheet">
<style>
  :root {
    --page-bg: #d8d3ce;
    --card-frost: #ecebe8;
    --card-frost-edge: #dcdad6;
    --accent-orange: #e2461d;
    --accent-orange-dark: #c9330f;
    --band-dark: #1f1f1f;
    --ink-dark: #1c1c1c;
    --ink-light: #e6e6e6;
    --name-light: #f1d9cc;
  }
  * { margin: 0; padding: 0; box-sizing: border-box; }
  html, body {
    width: 1200px; height: 970px; overflow: hidden;
    background: var(--page-bg);
    font-family: "Roboto", Arial, sans-serif;
  }
  .card {
    position: absolute; left: 80px; top: 189px;
    width: 1040px; height: 592px;
    border-radius: 26px; overflow: hidden;
    background: linear-gradient(180deg, var(--card-frost) 0%, var(--card-frost-edge) 100%);
    box-shadow: 0 18px 40px rgba(0,0,0,0.18);
  }
  .brand {
    position: absolute; left: 64px; top: 96px;
    display: flex; align-items: center; gap: 18px;
  }
  .brand-name {
    font-weight: 700; font-size: 66px; letter-spacing: -1px;
    color: var(--ink-dark); line-height: 1;
  }
  .brand-dot {
    width: 30px; height: 30px; border-radius: 50%;
    background: var(--accent-orange);
  }
  .card-bands { position: absolute; left: 0; top: 0; }
  .name-row {
    position: absolute; left: 66px; top: 314px;
    display: flex; align-items: center; color: var(--name-light);
  }
  .person-name { font-weight: 700; font-size: 30px; }
  .divider { width: 2px; height: 34px; background: var(--name-light); margin: 0 18px; }
  .person-title { font-weight: 400; font-size: 24px; }
  .address {
    position: absolute; left: 66px; top: 378px;
    color: var(--ink-light); font-size: 24px; line-height: 34px;
  }
  .contacts {
    position: absolute; left: 68px; top: 458px;
    list-style: none; color: var(--ink-light); font-size: 24px;
  }
  .contacts li { display: flex; align-items: center; height: 34px; }
  .contacts svg { width: 20px; height: 20px; margin-right: 14px; }
  .mark-area { position: absolute; left: 0; top: 0; }
</style>
</head>
<body>
  <div class="card">
    <svg class="card-bands" width="1040" height="592" viewBox="0 0 1040 592">
      <defs>
        <linearGradient id="bandOrange" x1="0" y1="0" x2="1" y2="0">
          <stop offset="0" stop-color="#e04a22"/>
          <stop offset="1" stop-color="#c42d0c"/>
        </linearGradient>
        <linearGradient id="markFill" x1="0" y1="0" x2="1" y2="1">
          <stop offset="0" stop-color="#f1efec"/>
          <stop offset="1" stop-color="#dedbd7"/>
        </linearGradient>
      </defs>
      <polygon points="0,304 845,304 810,360 0,360" fill="url(#bandOrange)"/>
      <rect x="0" y="363" width="1040" height="229" fill="var(--band-dark)"/>
      <g class="mark-area" role="img" aria-label="Soft decorative area where the brand swirl accent sits">
        <path d="M470,592 C480,520 560,470 650,470 C690,400 740,360 790,360 L1040,360 L1040,592 Z" fill="url(#markFill)" opacity="0.9"/>
      </g>
    </svg>

    <div class="brand">
      <span class="brand-name">Stonebrook 720</span>
      <span class="brand-dot"></span>
    </div>

    <div class="name-row">
      <span class="person-name">Daniel Furlow</span>
      <span class="divider"></span>
      <span class="person-title">Managing Partner</span>
    </div>

    <div class="address">
      <p>48317 Whitfield Lane</p>
      <p>Suite 510, Tampa, FL 33718</p>
    </div>

    <ul class="contacts">
      <li>
        <svg viewBox="0 0 20 20" aria-hidden="true"><rect x="5" y="1.5" width="10" height="17" rx="2" fill="none" stroke="#e2461d" stroke-width="2"/><rect x="8" y="14.5" width="4" height="1.6" fill="#e2461d"/></svg>
        813-555-4870
      </li>
      <li>
        <svg viewBox="0 0 20 20" aria-hidden="true"><rect x="1" y="4" width="18" height="12" fill="#e2461d"/><path d="M1,4 L10,11 L19,4" fill="none" stroke="#1f1f1f" stroke-width="1.5"/></svg>
        dfurlow@stonebrook720.example
      </li>
      <li>
        <svg viewBox="0 0 20 20" aria-hidden="true"><circle cx="10" cy="10" r="8" fill="none" stroke="#e2461d" stroke-width="1.8"/><ellipse cx="10" cy="10" rx="3.5" ry="8" fill="none" stroke="#e2461d" stroke-width="1.4"/><line x1="2" y1="10" x2="18" y2="10" stroke="#e2461d" stroke-width="1.4"/></svg>
        www.stonebrook720.example
      </li>
    </ul>
  </div>
</body>
</html>
```